Legal Stationary

A full set of stationery is required
The image and logo, along with colour, are set and attached.
The style should be modern, clean, and corporate. Not just a basic template off the web.
In addition to the address/website/email/phone fields for DX and KWT number, with the text “the firm is authorised and regulated by the KWT”
All files in all formats will be needed to allow editing after. Initial setup of templates will be required, and details for 4 business cards will be supplied.
Target Market(s)
Consumers of legal services
Industry/Entity Type
Legal

```html
<!DOCTYPE html>
<html lang="en">
<head>
<meta charset="utf-8">
<title>Halden Law Stationery</title>
<link href="https://fonts.googleapis.com/css2?family=Poppins:wght@400;500;600&display=swap" rel="stylesheet">
<style>
:root{
  --brand:#243d91;
  --ink:#111111;
  --paper:#ffffff;
  --stage:#cfd5d6;
  --ghost:#e6e8f2;
}
*{margin:0;padding:0;box-sizing:border-box}
html,body{width:1200px;height:842px;overflow:hidden;background:var(--stage);font-family:'Poppins',sans-serif;color:var(--ink)}
.sheet{position:absolute;background:var(--paper);overflow:hidden}
.band{position:absolute;left:0;top:0}
.wordmark{position:absolute;font-family:'Poppins',sans-serif;font-weight:600;color:var(--brand);white-space:nowrap;letter-spacing:.02em;line-height:1}
.wordmark--light{color:var(--paper)}
.contact{position:absolute;line-height:1.25}
.contact li{list-style:none;display:flex;align-items:center;gap:5px;white-space:nowrap}
.icon{width:1em;height:1em;flex:none;fill:var(--brand)}
.reg{position:absolute;left:0;width:100%;text-align:center;white-space:nowrap}

/* letterhead */
.letterhead{left:111px;top:65px;width:497px;height:702px}
.letterhead .wordmark{left:26px;top:40px;font-size:30px}
.letterhead .contact{right:27px;top:23px;font-size:11px;text-align:right}
.letterhead .contact li{justify-content:flex-end}
.letterhead .contact li.gap{margin-top:4px;align-items:flex-start}
.letterhead .contact .icon{margin-left:8px;order:2}
.letterhead .ghost-mark{left:0;width:100%;text-align:center;top:322px;font-size:52px;color:var(--ghost);font-weight:600}
.letterhead .reg{top:679px;font-size:10.5px;color:var(--paper);letter-spacing:.05em}

/* business cards */
.card{width:277px;height:159px}
.card-front{left:731px;top:65px;background:var(--brand)}
.card-front .wordmark{left:0;width:100%;text-align:center;top:65px;font-size:28px}
.card-front .reg{top:139px;font-size:7px;color:var(--paper)}
.card-back{left:731px;top:239px}
.card-back .wordmark{left:0;width:100%;text-align:center;top:14px;font-size:22px}
.person{position:absolute;right:147px;top:75px;text-align:right}
.person__name{font-size:14px;color:var(--brand);line-height:1.1}
.person__name b{font-weight:600}
.person__title{font-size:7.5px;font-weight:500}
.divider{position:absolute;left:138px;top:70px;width:1px;height:42px;background:var(--brand)}
.card-back .contact{left:153px;top:75px;font-size:7.2px;line-height:1.4}
.card-back .dx{position:absolute;top:116px;font-size:7px;color:var(--brand)}
.card-back .address{top:139px;font-size:7.5px;color:var(--paper)}

/* envelope */
.envelope-front{left:686px;top:423px;width:373px;height:166px}
.envelope-front .wordmark{right:10px;top:14px;font-size:17px}
.envelope-front .contact{left:250px;top:57px;font-size:7.2px;line-height:1.25}
.envelope-front .contact li.gap{margin-top:5px;align-items:flex-start}
.envelope-front .reg{top:150px;font-size:7px;color:var(--paper);letter-spacing:.04em}
.envelope-back{left:689px;top:606px;width:370px;height:165px}
.flap{position:absolute;left:4px;top:0;width:362px;height:56px;border-radius:0 0 14px 14px;background:var(--paper);box-shadow:0 4px 8px rgba(0,0,0,.12)}
.envelope-back .wordmark{left:0;width:100%;text-align:center;top:25px;font-size:7px}
</style>
</head>
<body>

<svg width="0" height="0" style="position:absolute">
  <symbol id="i-phone" viewBox="0 0 24 24"><path d="M6.6 10.8a15 15 0 0 0 6.6 6.6l2.2-2.2c.3-.3.7-.4 1-.2 1.1.4 2.3.6 3.6.6.6 0 1 .4 1 1V20c0 .6-.4 1-1 1A17 17 0 0 1 3 4c0-.6.4-1 1-1h3.5c.6 0 1 .4 1 1 0 1.3.2 2.5.6 3.6.1.3 0 .7-.2 1z"/></symbol>
  <symbol id="i-globe" viewBox="0 0 24 24"><path d="M12 2a10 10 0 1 0 0 20 10 10 0 0 0 0-20zm6.9 6h-3a15 15 0 0 0-1.3-3.9A8 8 0 0 1 18.9 8zM12 4c.8 1.2 1.5 2.5 1.9 4h-3.8c.4-1.5 1.1-2.8 1.9-4zM4.3 14a8 8 0 0 1 0-4h3.4a16 16 0 0 0 0 4zm.8 2h3a15 15 0 0 0 1.3 3.9A8 8 0 0 1 5.1 16zm3-8h-3a8 8 0 0 1 4.3-3.9C8.8 5.3 8.4 6.6 8.1 8zM12 20c-.8-1.2-1.5-2.5-1.9-4h3.8c-.4 1.5-1.1 2.8-1.9 4zm2.3-6H9.7a14 14 0 0 1 0-4h4.6a14 14 0 0 1 0 4zm.3 5.9c.6-1.2 1-2.5 1.3-3.9h3a8 8 0 0 1-4.3 3.9zm1.7-5.9a16 16 0 0 0 0-4h3.4a8 8 0 0 1 0 4z"/></symbol>
  <symbol id="i-mail" viewBox="0 0 24 24"><path d="M3 9l9-6 9 6v11H3zm2 1.6V18h14v-7.4l-7 4.6zM6 9l6 4 6-4-6-4z"/></symbol>
  <symbol id="i-pin" viewBox="0 0 24 24"><path d="M12 2a7 7 0 0 0-7 7c0 5 7 11 7 11s7-6 7-11a7 7 0 0 0-7-7zm0 9.5A2.5 2.5 0 1 1 12 6.5a2.5 2.5 0 0 1 0 5zM6 21h12v1.5H6z"/></symbol>
</svg>

<!-- Letterhead -->
<section class="sheet letterhead" aria-label="Letterhead">
  <div class="wordmark">HALDEN LAW</div>
  <ul class="contact">
    <li>(555) 014-2288<svg class="icon"><use href="#i-phone"/></svg></li>
    <li>info@haldenlaw.example<svg class="icon"><use href="#i-globe"/></svg></li>
    <li>www.haldenlaw.example<svg class="icon"><use href="#i-mail"/></svg></li>
    <li class="gap">418 Elmstead Ave. Suite<br>300 Riverton, TX 75001<svg class="icon"><use href="#i-pin"/></svg></li>
  </ul>
  <div class="wordmark ghost-mark">HALDEN LAW</div>
  <svg class="band" width="497" height="702" viewBox="0 0 497 702">
    <path d="M0 632 Q248 728 497 632 L497 702 L0 702Z" fill="var(--brand)"/>
    <path d="M18 628 Q248 720 479 628 Q248 708 18 628Z" fill="var(--ink)"/>
  </svg>
  <p class="reg">DX-4821&nbsp;&nbsp;KWT-00 47 318 260</p>
</section>

<!-- Business card front -->
<section class="sheet card card-front" aria-label="Business card front">
  <div class="wordmark wordmark--light">HALDEN LAW</div>
  <p class="reg">The Firm is Authorised and Regulated by the KWT</p>
</section>

<!-- Business card back -->
<section class="sheet card card-back" aria-label="Business card back">
  <div class="wordmark">HALDEN LAW</div>
  <div class="person">
    <p class="person__name"><b>Marta</b> Kovel</p>
    <p class="person__title">Founder &amp; CEO</p>
  </div>
  <div class="divider"></div>
  <ul class="contact">
    <li><svg class="icon"><use href="#i-phone"/></svg>(555) 014-2288</li>
    <li><svg class="icon"><use href="#i-globe"/></svg>info@haldenlaw.example</li>
    <li><svg class="icon"><use href="#i-mail"/></svg>www.haldenlaw.example</li>
  </ul>
  <svg class="band" width="277" height="159" viewBox="0 0 277 159">
    <path d="M0 112 Q138 156 277 112 L277 159 L0 159Z" fill="var(--brand)"/>
    <path d="M10 111 Q138 154 267 111 Q138 148 10 111Z" fill="var(--ink)"/>
  </svg>
  <p class="reg dx">DX-4821 &amp; KWT-00 47 318 260</p>
  <p class="reg address">418 Elmstead Ave. Suite 300 Riverton, TX 75001</p>
</section>

<!-- Envelope front -->
<section class="sheet envelope-front" aria-label="Envelope front">
  <div class="wordmark">HALDEN LAW</div>
  <ul class="contact">
    <li><svg class="icon"><use href="#i-phone"/></svg>(555) 014-2288</li>
    <li><svg class="icon"><use href="#i-mail"/></svg>info@haldenlaw.example</li>
    <li><svg class="icon"><use href="#i-globe"/></svg>www.haldenlaw.example</li>
    <li class="gap"><svg class="icon"><use href="#i-pin"/></svg>418 Elmstead Ave. Suite<br>300 Riverton, TX 75001</li>
  </ul>
  <svg class="band" width="373" height="166" viewBox="0 0 373 166">
    <path d="M0 111 Q186 176 373 111 L373 166 L0 166Z" fill="var(--brand)"/>
    <path d="M12 110 Q186 170 361 110 Q186 162 12 110Z" fill="var(--ink)"/>
  </svg>
  <p class="reg">DX-4821&nbsp;&nbsp;KWT-00 47 318 260</p>
</section>

<!-- Envelope back -->
<section class="sheet envelope-back" aria-label="Envelope back">
  <div class="flap"></div>
  <div class="wordmark">HALDEN LAW</div>
</section>

</body>
</html>
```